Commercial Swimming Pool - Design-Build Contractor Website Design

I need a new website that will feature our newly developed logo and trade name as well as provide a fully updated site experience. We are not a residential builder - we strictly design and install high-end commercial pools. I need the website to highlight our portfolio and communicate the various types of projects in which we specialize. I want the effect of the site to reflect the high-end nature of our services - projects like the 57th floor spa at the Phila Tall Cedars, the aquatic therapy portion of the Phila Quillers training facility, a 5om indoor competition pool for the prestigious Draymoor Academy, the indoor water park at The Brackwell Lodge or the recent country club renovation projects we've completed in our region (to name a few examples).

```html
<!DOCTYPE html>
<html lang="en">
<head>
<meta charset="utf-8">
<title>Corwell Aquatics – Commercial Pools</title>
<link href="https://fonts.googleapis.com/css2?family=Poppins:wght@400;500;600;700;800&display=swap" rel="stylesheet">
<style>
:root{
  --navy:#0b1a5c;
  --navy-deep:#08144a;
  --blue:#1e8fd6;
  --sky:#57c3ee;
  --orange:#f7a21b;
  --grey:#dcdcdc;
  --ink:#1b1b1b;
  --ghost:#ececec;
  --white:#ffffff;
  --foot-bar:#5fc2ec;
}
*{margin:0;padding:0;box-sizing:border-box}
html,body{width:1200px;height:5292px;overflow:hidden}
body{font-family:"Poppins",sans-serif;color:var(--ink);background:var(--white);position:relative}
.abs{position:absolute}
.photo{position:absolute}
.btn{position:absolute;display:flex;align-items:center;justify-content:center;border-radius:30px;font-weight:600;text-transform:uppercase;color:var(--white);letter-spacing:.5px}

/* brand */
.brand{position:absolute;display:flex;align-items:center;gap:12px}
.brand-mark{width:40px;height:40px;background:var(--blue);flex:none}
.brand-name{display:flex;flex-direction:column;font-weight:700;color:var(--navy);text-transform:uppercase;line-height:.95}

/* header */
.site-header{position:absolute;left:0;top:0;width:1200px;height:160px;background:var(--white)}
.site-header .brand{left:60px;top:46px}
.site-header .brand-name{font-size:32px}
.main-nav{position:absolute;left:388px;top:68px;display:flex;gap:34px;font-size:16px;font-weight:500;color:var(--navy);text-transform:uppercase}
.header-cta{left:956px;top:58px;width:180px;height:44px;background:var(--navy);font-size:15px}

/* hero */
.hero{position:absolute;left:0;top:160px;width:1200px;height:700px;background:linear-gradient(180deg,#7fa7a2 0%,#5f8f8c 30%,#1aa6c5 55%,#0b7ea8 80%,#0a5e85 100%)}
.hero-title{position:absolute;left:0;width:1200px;text-align:center;color:var(--white);font-weight:800;text-transform:uppercase;text-shadow:0 3px 10px rgba(0,0,0,.35)}
.hero-title.l1{top:530px;font-size:76px;letter-spacing:2px}
.hero-title.l2{top:618px;font-size:62px}
.hero-cta{left:496px;top:712px;width:208px;height:58px;background:var(--orange);font-size:16px}

/* section headings */
.ghost{position:absolute;left:0;width:1200px;text-align:center;font-weight:800;color:var(--ghost);text-transform:uppercase;letter-spacing:8px;font-size:140px;line-height:1}
.sec-title{position:absolute;left:0;width:1200px;text-align:center;font-weight:600;color:var(--navy);text-transform:uppercase;font-size:50px;line-height:1}

/* project cards */
.card{position:absolute;width:300px;height:450px;background:var(--white);box-shadow:0 4px 18px rgba(0,0,0,.16)}
.card .photo{left:12px;top:14px;width:276px;height:210px}
.card h3{position:absolute;left:0;top:250px;width:300px;text-align:center;color:var(--navy);font-size:18px;font-weight:700;text-transform:uppercase}
.card p{position:absolute;left:40px;top:290px;width:220px;text-align:center;font-size:13px;line-height:17px}
.card .btn{left:98px;top:372px;width:104px;height:32px;font-size:12px;background:var(--navy)}
.card .btn.alt{background:var(--sky)}

/* about */
.about-photo{left:0;top:1580px;width:1200px;height:650px;background:linear-gradient(180deg,#d8c9ad 0%,#b9a787 22%,#4fb0d6 45%,#2e94c6 62%,#cfe7f3 84%,#ffffff 100%)}
.about-copy{position:absolute;left:190px;top:1940px;width:820px;text-align:center;font-size:16px;line-height:30px}
.about-cta{left:526px;top:2104px;width:148px;height:40px;background:var(--navy);font-size:14px}

/* services */
.services{position:absolute;left:0;top:2220px;width:1200px;height:1172px;background:var(--grey)}
.services .ghost{color:#f4f4f4}
.svc{position:absolute;width:480px;height:380px;background:var(--white);box-shadow:0 4px 16px rgba(0,0,0,.14)}
.svc h3{position:absolute;left:30px;width:420px;text-align:center;color:var(--navy);font-weight:700;font-size:24px;line-height:30px;text-transform:uppercase}
.svc .photo{left:12px;width:456px;height:220px}
.svc-feature{position:absolute;left:416px;top:2732px;width:372px;height:308px;background:var(--white);border:8px solid var(--sky);box-shadow:0 6px 20px rgba(0,0,0,.18)}
.svc-feature h3{position:absolute;left:10px;top:14px;width:340px;text-align:center;color:var(--navy);font-weight:700;font-size:26px;line-height:32px;text-transform:uppercase}
.svc-feature .photo{left:14px;top:100px;width:328px;height:188px}

/* portfolio */
.dots{position:absolute;display:flex;gap:8px}
.dots span{width:14px;height:14px;border-radius:50%;background:var(--blue)}
.dots span.on{background:var(--navy)}

/* testimonials */
.testi{position:absolute;left:0;top:4336px;width:1200px;height:640px;background:linear-gradient(180deg,#8ccfee 0%,#b9e2f5 40%,#dff2fb 100%)}
.testi .ghost{color:rgba(255,255,255,.55);font-size:110px;letter-spacing:4px;top:56px}
.quote-mark{position:absolute;font-size:64px;font-weight:800;color:var(--navy);line-height:1}
.quote-text{position:absolute;left:230px;top:4530px;width:740px;text-align:center;font-size:16px;line-height:24px}
.avatar{position:absolute;left:364px;top:4636px;width:130px;height:130px;border-radius:50%;background:linear-gradient(180deg,#e9e4df,#c9bfb6);border:6px solid var(--white)}
.client-name{position:absolute;left:510px;top:4722px;font-size:16px;font-weight:500}

/* footer */
.site-footer{position:absolute;left:0;top:4900px;width:1200px;height:320px;background:var(--navy-deep)}
.site-footer .brand{left:100px;top:60px}
.site-footer .brand-mark{background:var(--sky)}
.site-footer .brand-name{color:var(--white);font-size:38px}
.social{position:absolute;left:150px;top:182px;display:flex;gap:24px}
.social span{width:44px;height:44px;border-radius:50%;background:var(--blue)}
.foot-col h4{position:absolute;color:var(--white);font-size:16px;font-weight:600}
.quick-links{position:absolute;left:556px;top:90px;list-style:none;color:var(--white);font-size:14px;line-height:26px}
.quick-links li::before{content:"›";margin-right:8px}
.contact-row{position:absolute;left:776px;display:flex;align-items:flex-start;gap:14px;color:var(--white);font-size:14px;line-height:20px}
.contact-row .ico{width:36px;height:36px;border-radius:50%;background:var(--white);flex:none;display:flex;align-items:center;justify-content:center}
.copyright{position:absolute;left:0;top:5220px;width:1200px;height:72px;background:var(--foot-bar);text-align:center;font-size:13px;line-height:72px;color:var(--navy-deep)}
</style>
</head>
<body>

<header class="site-header">
  <div class="brand"><span class="brand-mark"></span><span class="brand-name"><span>Corwell</span><span>Aquatics</span></span></div>
  <nav class="main-nav"><span>Home</span><span>About Us</span><span>Projects ▾</span><span>Portfolio</span><span>Testimonials</span><span>Contact</span></nav>
  <div class="btn header-cta">Request a Quote</div>
</header>

<section class="hero" role="img" aria-label="Hotel rooftop pool with white parasols and lounge chairs"></section>
<div class="hero-title l1">Design and Install</div>
<div class="hero-title l2">High-End Commercial Pools</div>
<div class="btn hero-cta">Request a Quote</div>
<svg class="abs" style="left:0;top:790px" width="1200" height="80" viewBox="0 0 1200 80" preserveAspectRatio="none"><path d="M0 40 C200 0 400 70 600 40 C800 10 1000 70 1200 30 L1200 80 L0 80Z" fill="#fff"/></svg>

<!-- projects -->
<div class="ghost" style="top:866px">Projects</div>
<h2 class="sec-title" style="top:948px">We Specialize In</h2>

<article class="card" style="left:108px;top:1032px">
  <div class="photo" role="img" aria-label="Blue outdoor commercial pool" style="background:linear-gradient(180deg,#3aa6d8,#1c7fb9)"></div>
  <svg class="abs" style="left:12px;top:194px" width="276" height="32" viewBox="0 0 276 32" preserveAspectRatio="none"><path d="M0 16 C70 0 140 32 276 10 L276 32 L0 32Z" fill="#fff"/></svg>
  <h3>Lorem Ipsum Dolor</h3>
  <p>Lorem ipsum dolor sit amet, consectetur adipiscing elit, sed do eiusmod tempor incididunt.</p>
  <div class="btn">Read More</div>
</article>
<article class="card" style="left:450px;top:1032px">
  <div class="photo" role="img" aria-label="Resort pool surrounded by buildings" style="background:linear-gradient(180deg,#c9d6e0 0%,#9fb3c3 35%,#3db4e2 60%,#1f8fc8 100%)"></div>
  <svg class="abs" style="left:12px;top:194px" width="276" height="32" viewBox="0 0 276 32" preserveAspectRatio="none"><path d="M0 16 C70 0 140 32 276 10 L276 32 L0 32Z" fill="#fff"/></svg>
  <h3>Lorem Ipsum Dolor</h3>
  <p>Lorem ipsum dolor sit amet, consectetur adipiscing elit, sed do eiusmod tempor incididunt.</p>
  <div class="btn alt">Read More</div>
</article>
<article class="card" style="left:792px;top:1032px">
  <div class="photo" role="img" aria-label="Aerial view of a swimmer in a turquoise pool" style="background:linear-gradient(160deg,#2ec2c9,#139aa9)"></div>
  <svg class="abs" style="left:12px;top:194px" width="276" height="32" viewBox="0 0 276 32" preserveAspectRatio="none"><path d="M0 16 C70 0 140 32 276 10 L276 32 L0 32Z" fill="#fff"/></svg>
  <h3>Lorem Ipsum Dolor</h3>
  <p>Lorem ipsum dolor sit amet, consectetur adipiscing elit, sed do eiusmod tempor incididunt.</p>
  <div class="btn">Read More</div>
</article>

<!-- about -->
<div class="photo about-photo" role="img" aria-label="Outdoor pool with lounge chairs behind a white fence"></div>
<div class="ghost" style="top:1800px;color:rgba(255,255,255,.6)">About</div>
<h2 class="sec-title" style="top:1862px;font-size:56px;font-weight:700">Corwell Aquatics</h2>
<p class="about-copy">Lorem ipsum dolor sit amet, consectetur adipiscing elit, sed do eiusmod tempor incididunt ut labore et dolore magna aliqua. Ut enim ad minim veniam, quis nostrud exercitation ullamco laboris nisi ut aliquip ex ea commodo consequat. Duis aute irure dolor in reprehenderit in voluptate velit esse cillum dolore eu fugiat nulla pariatur. Excepteur sint</p>
<div class="btn about-cta">Read More</div>

<!-- services -->
<section class="services">
  <div class="ghost" style="top:66px">High End</div>
  <h2 class="sec-title" style="top:130px">Nature of Services</h2>
</section>

<article class="svc" style="left:108px;top:2440px">
  <h3 style="top:44px">The 57th Floor Spa at the Phila Tall Cedars</h3>
  <div class="photo" role="img" aria-label="Indoor rooftop spa pool" style="top:150px;background:linear-gradient(180deg,#8a7a62,#5f8f86 60%,#3a6f6a)"></div>
  <svg class="abs" style="left:12px;top:140px" width="456" height="40" viewBox="0 0 456 40" preserveAspectRatio="none"><path d="M0 0 L456 0 L456 14 C340 40 200 0 0 30Z" fill="#fff"/></svg>
</article>
<article class="svc" style="left:628px;top:2440px">
  <h3 style="top:44px">The Aquatic Therapy Portion of the Phila Quillers Training Facility</h3>
  <div class="photo" role="img" aria-label="Therapy pool session in clear water" style="top:150px;background:linear-gradient(180deg,#9fd8ef,#4fb5df)"></div>
  <svg class="abs" style="left:12px;top:140px" width="456" height="40" viewBox="0 0 456 40" preserveAspectRatio="none"><path d="M0 0 L456 0 L456 14 C340 40 200 0 0 30Z" fill="#fff"/></svg>
</article>
<article class="svc" style="left:108px;top:2860px">
  <div class="photo" role="img" aria-label="Indoor water park with slides" style="top:12px;background:linear-gradient(180deg,#7fc2e6,#2f9fd3 60%,#3f8f5f)"></div>
  <svg class="abs" style="left:12px;top:200px" width="456" height="40" viewBox="0 0 456 40" preserveAspectRatio="none"><path d="M0 14 C150 40 300 0 456 26 L456 40 L0 40Z" fill="#fff"/></svg>
  <h3 style="top:276px">The Indoor Water Park at The Brackwell Lodge</h3>
</article>
<article class="svc" style="left:628px;top:2860px">
  <div class="photo" role="img" aria-label="Competition swimmer in a lane pool" style="top:12px;background:linear-gradient(180deg,#3fb4e6,#1a86c8)"></div>
  <svg class="abs" style="left:12px;top:200px" width="456" height="40" viewBox="0 0 456 40" preserveAspectRatio="none"><path d="M0 14 C150 40 300 0 456 26 L456 40 L0 40Z" fill="#fff"/></svg>
  <h3 style="top:262px">A 50M Indoor Competition Pool for the Prestigious Draymoor Academy</h3>
</article>
<article class="svc-feature">
  <h3>Country Club Renovation Project</h3>
  <div class="photo" role="img" aria-label="Renovated country club pool with clubhouse" style="background:linear-gradient(180deg,#b7a796,#8a7464 40%,#35a9dc 65%,#1f8fc8)"></div>
</article>

<!-- portfolio -->
<div class="ghost" style="top:3440px">Gallery</div>
<h2 class="sec-title" style="top:3508px">Our Portfolio</h2>
<div class="photo" role="img" aria-label="Seaside resort infinity pool with palm trees" style="left:100px;top:3608px;width:655px;height:272px;background:linear-gradient(180deg,#a9d3ee,#5fa7c8 40%,#2fa3cf 70%,#1d7fa8)"></div>
<div class="photo" role="img" aria-label="Indoor pool with tiled walls and blue lane water" style="left:775px;top:3608px;width:325px;height:560px;background:linear-gradient(180deg,#d9cfc3,#bfb0a0 25%,#5ab8e4 50%,#2d8ed0)"></div>
<div class="photo" role="img" aria-label="Hotel courtyard pool in daylight" style="left:100px;top:3896px;width:320px;height:272px;background:linear-gradient(180deg,#c8b9a4,#3bb1d6 55%,#1d8db4)"></div>
<div class="photo" role="img" aria-label="Pool lit up at night" style="left:435px;top:3896px;width:320px;height:272px;background:linear-gradient(180deg,#0d1c3b,#1e3f7a 50%,#1c7ad1)"></div>
<div class="dots" style="left:563px;top:4216px"><span class="on"></span><span></span><span></span><span></span></div>

<!-- testimonials -->
<section class="testi">
  <div class="ghost">Testimonials</div>
  <h2 class="sec-title" style="top:106px">Our Client Says</h2>
</section>
<div class="quote-mark" style="left:170px;top:4516px">“</div>
<p class="quote-text">Lorem ipsum dolor sit amet, consectetur adipiscing elit, sed do eiusmod tempor incididunt ut labore et dolore magna aliqua. Ut enim ad minim veniam, quis nostrud exercitation ullamco laboris nisi ut aliquip ex ea commodo consequat. Duis aute irure dolor in reprehenderit in</p>
<div class="quote-mark" style="left:990px;top:4590px">”</div>
<div class="avatar" role="img" aria-label="Client portrait"></div>
<div class="client-name">Dale Merriton, Stock Car Driver</div>
<div class="dots" style="left:570px;top:4850px"><span></span><span class="on"></span><span></span></div>
<svg class="abs" style="left:0;top:4870px" width="1200" height="60" viewBox="0 0 1200 60" preserveAspectRatio="none"><path d="M0 30 C300 0 600 60 900 24 C1020 10 1120 20 1200 30 L1200 60 L0 60Z" fill="#08144a"/></svg>

<!-- footer -->
<footer class="site-footer">
  <div class="brand"><span class="brand-mark"></span><span class="brand-name"><span>Corwell</span><span>Aquatics</span></span></div>
  <div class="social" aria-label="Social links"><span></span><span></span><span></span><span></span></div>
  <div class="foot-col"><h4 style="left:536px;top:56px">Quick Links</h4></div>
  <ul class="quick-links"><li>Home</li><li>About Us</li><li>Projects</li><li>Portfolio</li><li>Testimonials</li><li>Contact</li></ul>
  <div class="foot-col"><h4 style="left:776px;top:56px">Contact Us</h4></div>
  <div class="contact-row" style="top:100px"><span class="ico"><svg width="18" height="18" viewBox="0 0 24 24"><path d="M12 2a7 7 0 0 0-7 7c0 5 7 13 7 13s7-8 7-13a7 7 0 0 0-7-7zm0 9.5A2.5 2.5 0 1 1 12 6.5a2.5 2.5 0 0 1 0 5z" fill="#08144a"/></svg></span><span>Location Name<br>Dummy Address Here<br>PA 123456</span></div>
  <div class="contact-row" style="top:176px"><span class="ico"><svg width="18" height="18" viewBox="0 0 24 24"><path d="M6.6 10.8a15 15 0 0 0 6.6 6.6l2.2-2.2a1 1 0 0 1 1-.25 11.4 11.4 0 0 0 3.6.57 1 1 0 0 1 1 1V20a1 1 0 0 1-1 1A17 17 0 0 1 3 4a1 1 0 0 1 1-1h3.5a1 1 0 0 1 1 1c0 1.25.2 2.450.57 3.57a1 1 0 0 1-.25 1z" fill="#08144a"/></svg></span><span>123 456 7890<br>258 963 7410</span></div>
  <div class="contact-row" style="top:240px"><span class="ico"><svg width="18" height="18" viewBox="0 0 24 24"><path d="M3 5h18v14H3z" fill="none" stroke="#08144a" stroke-width="2"/><path d="M3 6l9 7 9-7" fill="none" stroke="#08144a" stroke-width="2"/></svg></span><span style="line-height:36px">Email: hello@corwellaquatics.com</span></div>
</footer>
<div class="copyright">Copyright © 2023 All rights reserved.</div>

</body>
</html>
```